Business card for STEADYWAVE

Please design professional business card for IT consulting firm STEADYWAVE INC.
Use logo attached.
Use information from sample qNode business card attached.
replace qnode inc with STEADYWAVE INC.
as well as qnodeinc.com with steadywave.example

```html
<!DOCTYPE html>
<html lang="en">
<head>
<meta charset="utf-8">
<title>STEADYWAVE INC. — Business Card</title>
<link rel="stylesheet" href="https://fonts.googleapis.com/css2?family=Inter:wght@400;500&family=Montserrat:wght@700&display=swap">
<style>
  :root {
    --stage: #2b2b2d;
    --card: #ffffff;
    --ink: #111111;
    --muted: #2a2a2a;
    --accent-orange: #e8821e;
    --grad-purple: #9b3fb0;
    --grad-teal: #3fc0c0;
    --grad-blue: #4a62c9;
    --shadow: rgba(0,0,0,0.45);
  }
  * { box-sizing: border-box; margin: 0; padding: 0; }
  html, body {
    width: 1200px; height: 900px; overflow: hidden;
    background: var(--stage);
    font-family: "Inter", Arial, sans-serif;
    color: var(--ink);
  }
  .stage { position: relative; width: 1200px; height: 900px; }
  .card {
    position: absolute; left: 290px;
    width: 620px; height: 354px;
    background: var(--card);
    box-shadow: 0 12px 28px var(--shadow);
    overflow: hidden;
  }
  .card--front { top: 80px; }
  .card--back  { top: 470px; }

  .wordmark {
    position: absolute;
    font-family: "Montserrat", Arial, sans-serif;
    font-weight: 700;
    letter-spacing: 0.14em;
    color: var(--ink);
    white-space: nowrap;
  }
  .card--front .wordmark { right: 56px; top: 188px; font-size: 32px; }
  .card--back .wordmark  { right: 44px; top: 70px; font-size: 30px; }

  .holder {
    position: absolute; left: 44px; top: 176px;
    font-size: 21px; font-weight: 500; letter-spacing: -0.02em;
    text-transform: uppercase; white-space: nowrap;
  }
  .holder .credential {
    font-size: 12px; font-weight: 400; color: var(--accent-orange);
    letter-spacing: 0; margin-left: 2px;
  }
  .divider {
    position: absolute; left: 44px; right: 44px; top: 206px; height: 2px;
    background: linear-gradient(90deg,
      var(--grad-purple) 0%, var(--grad-teal) 14%, var(--grad-blue) 26%,
      var(--accent-orange) 38%, var(--grad-blue) 58%, var(--grad-teal) 74%,
      var(--grad-purple) 100%);
  }
  .contact {
    position: absolute; list-style: none;
    font-size: 14px; color: var(--muted); letter-spacing: -0.01em;
    white-space: nowrap;
  }
  .contact li { display: flex; align-items: center; gap: 8px; height: 20px; }
  .contact li.gap { margin-top: 10px; }
  .contact svg { width: 13px; height: 13px; flex: none; }
  .contact--left { left: 50px; top: 230px; }
  .contact--right { left: 320px; top: 230px; }
  .contact--right li { align-items: flex-start; height: auto; line-height: 20px; }
  .contact--right svg { margin-top: 3px; }
</style>
</head>
<body>
<main class="stage">
  <section class="card card--front" aria-label="Card front">
    <div class="wordmark">STEADYWAVE INC</div>
  </section>

  <section class="card card--back" aria-label="Card back">
    <div class="wordmark">STEADYWAVE INC</div>
    <div class="holder">Dorian Velasko<span class="credential">, P.ENG.</span></div>
    <div class="divider"></div>

    <ul class="contact contact--left">
      <li>
        <svg viewBox="0 0 16 16"><rect x="4" y="1" width="8" height="14" rx="1.5" fill="none" stroke="#222" stroke-width="1.4"/></svg>
        (555) 014-2230
      </li>
      <li>
        <svg viewBox="0 0 16 16"><path d="M2 6c0-2 3-3.5 6-3.5S14 4 14 6l-2.5 1V5.5h-7V7L2 6zM4 8h8l1.5 6h-11z" fill="#222"/></svg>
        (555) 019-4410 ext.38
      </li>
      <li class="gap">
        <svg viewBox="0 0 16 16"><circle cx="8" cy="8" r="6" fill="none" stroke="#222" stroke-width="1.6"/><path d="M2 8h12M8 2c-2.5 3-2.5 9 0 12M8 2c2.5 3 2.5 9 0 12" fill="none" stroke="#222" stroke-width="1.1"/></svg>
        www.steadywave.example
      </li>
      <li>
        <svg viewBox="0 0 16 16"><rect x="1.5" y="4" width="13" height="9" fill="#222"/><path d="M1.5 4l6.5 5 6.5-5" fill="none" stroke="#fff" stroke-width="1.2"/></svg>
        dvelasko@steadywave.example
      </li>
    </ul>

    <ul class="contact contact--right">
      <li>
        <svg viewBox="0 0 16 16"><path d="M8 1a5 5 0 0 1 5 5c0 3.5-5 9-5 9S3 9.5 3 6a5 5 0 0 1 5-5z" fill="#222"/><circle cx="8" cy="6" r="2" fill="#fff"/></svg>
        <span>1820 Harbourline Rd, Unit 7<br>Northvale, Westmark, Z9Y 8X7, Norland</span>
      </li>
    </ul>
  </section>
</main>
</body>
</html>
```